New solo practice law firm is looking for an elegant, professional, and interactive web design

I need a web design and developer for a new small law firm in Sacramento, California called Dorian Kessel Law, A Professional Corporation. I am a trial lawyer who represents average people facing difficult litigation disputes, including criminal defense as a former prosecutor and civil litigation as a civil litigator. Criminal defense includes domestic violence, battery, assault, drug possession, theft, DUI, etc. Civil litigation includes business disputes, property disputes, employment disputes, family law disputes, and immigration issues. I would like to see web designs that incorporate my logo and use the logo's navy blue and gold colors. I have uploaded the files of my logo to this brief. Please only use the navy blue and gold version. Overall, I want the design to look firm, professional, and elegant.

I plan on having the following pages on my website: (1) Home, (2) Dorian Kessel, (3) Practice Areas, (4) Insights, (5) Contact. I've hand drawn a preliminary sketch concept of what I envision the home page's layout to look like (attached with a text version). I would like your design to keep a similar layout for the homepage and incorporate my logo's colors within it but I am open to creative layout alternatives/ideas. I would like the other pages to have a similar look and feel as the home page. Some of the areas currently in my sketch do not have the full text. You can insert other text for now and I will provide the winner the full text.

In terms of the pictures on the website, I enjoy images of courthouses, columns (example attached but I cannot use this one), and, if possible, images from Sacramento, CA in my background (headshot attached). A plus would be live images that move and also sections of the webpage moving in the viewers view as they scroll down on the page. Also, it would be great to have my logo act as the tab for the website. I can provide other versions of the logo if needed.

I look forward to seeing your Wordpress designs!

People needing legal representation.

Law

Coded - Design and coding required

5+ page

Serif

• Incorporate my logo and my logo's colors.
• Live pictures and images appearing as viewers scroll on page.

```html
<!DOCTYPE html>
<html lang="en">
<head>
<meta charset="utf-8">
<title>Dorian Kessel Law</title>
<link rel="stylesheet" href="https://fonts.googleapis.com/css2?family=Karla:wght@400;500;600;700&family=Nunito+Sans:wght@300;400;600;700&display=swap">
<style>
:root{
  --navy:#14213d;
  --navy-line:#2c3a57;
  --gold:#ad9461;
  --gold-light:#c4a96f;
  --ink:#1b2236;
  --muted:#5d6272;
  --paper:#f7f7f8;
  --mist:#eceef1;
  --white:#ffffff;
}
*{box-sizing:border-box;margin:0;padding:0}
html,body{width:1200px;height:2686px;overflow:hidden}
body{position:relative;font-family:"Nunito Sans",sans-serif;color:var(--ink);background:var(--white)}
.abs{position:absolute}
.topbar{left:0;top:0;width:1200px;height:44px;background:var(--gold);color:var(--white);font:700 12.5px "Nunito Sans",sans-serif;text-align:center;line-height:44px}
.header{left:0;top:44px;width:1200px;height:92px;background:var(--navy);border-bottom:1px solid var(--navy-line)}
.brand{display:flex;align-items:center;gap:14px;color:var(--white);font:500 14px "Karla",sans-serif;letter-spacing:2.4px;text-transform:uppercase;line-height:1.35}
.brand-mark{width:46px;height:46px;border:2px solid var(--white)}
.brand small{display:block;font-size:8.5px;letter-spacing:1.8px}
.header .brand{left:96px;top:21px}
.info{display:flex;align-items:center;gap:18px}
.info-label{color:var(--white);font:700 11px "Karla",sans-serif;letter-spacing:1px;text-transform:uppercase}
.info-value{color:var(--gold-light);font:600 18px "Karla",sans-serif;letter-spacing:.4px;margin-top:2px}
.nav{left:0;top:136px;width:1200px;height:55px;background:var(--navy)}
.nav a{position:absolute;top:0;line-height:55px;color:var(--white);font:700 13.5px "Karla",sans-serif;letter-spacing:1.2px;text-decoration:none;text-transform:uppercase}
.nav a.active{color:var(--gold)}
.hero{left:0;top:191px;width:1200px;height:412px;background:linear-gradient(180deg,#1d2744 0%,#2b3650 40%,#5a4b2a 72%,#1a2230 100%)}
.hero h1{position:absolute;left:0;width:1200px;top:148px;text-align:center;color:var(--white);font:500 45px/1.2 "Karla",sans-serif;letter-spacing:.5px}
.services{left:0;top:603px;width:1200px;height:685px;background:var(--paper)}
.card{width:229px;height:217px;background:var(--white);box-shadow:0 6px 24px rgba(20,33,61,.08);text-align:center}
.card svg{position:absolute;left:50%;transform:translateX(-50%)}
.card span{position:absolute;left:0;width:100%;font:500 16.5px "Karla",sans-serif;letter-spacing:.4px;color:var(--ink)}
.intro{left:682px;top:698px;width:440px}
.intro h2{font:500 21.5px/31px "Karla",sans-serif;color:var(--ink);letter-spacing:.2px}
.intro p{font:300 12.5px/21px "Nunito Sans",sans-serif;color:var(--muted);margin-top:22px}
.intro p+p{margin-top:20px}
.rule{height:1px;background:#d9dadf}
.call-label{font:600 12.5px "Karla",sans-serif;color:var(--ink)}
.call-phone{font:700 23px "Karla",sans-serif;color:var(--gold);letter-spacing:.5px}
.about{left:0;top:1288px;width:1200px;height:561px;background:linear-gradient(100deg,#a79e94 0%,#cfc8bf 35%,#b8b0a5 60%,#d8d2c9 100%)}
.portrait{left:680px;top:1288px;width:495px;height:561px;background:linear-gradient(180deg,#6d5a4c 0%,#3a3431 35%,#1e1e22 100%)}
.about-panel{left:79px;top:1421px;width:484px;height:294px;background:var(--mist);padding:40px 38px}
.about-panel h2{font:500 26px "Karla",sans-serif;color:var(--ink)}
.about-panel p{font:300 12.5px/21px "Nunito Sans",sans-serif;color:var(--muted);margin-top:14px}
.btn{display:inline-block;background:var(--gold);color:var(--white);font:700 13px "Karla",sans-serif;border-radius:3px;text-align:center}
.about-panel .btn{margin-top:22px;width:177px;height:41px;line-height:41px}
.consult{left:0;top:1849px;width:1200px;height:411px;background:var(--mist)}
.consult h2{position:absolute;left:75px;top:70px;font:600 27px "Karla",sans-serif;color:var(--ink);letter-spacing:.3px}
.field-label{font:400 13px "Karla",sans-serif;color:var(--ink)}
.field{background:var(--white);border:1px solid #d4d6dc;border-radius:3px;font:400 10.5px "Karla",sans-serif;color:var(--muted);padding:0 15px;display:flex;align-items:center}
.field.area{align-items:flex-start;padding-top:14px}
.submit{left:790px;top:2078px;width:334px;height:49px;line-height:49px;font-size:13px}
.footer{left:0;top:2260px;width:1200px;height:426px;background:var(--navy)}
.footer .brand{left:76px;top:60px}
.foot-head{font:400 14.5px "Karla",sans-serif;color:var(--gold);letter-spacing:.4px;text-transform:uppercase}
.foot-text{font:600 16px/21px "Karla",sans-serif;color:var(--white)}
.links a{display:block;color:var(--white);font:600 16px "Karla",sans-serif;text-decoration:none;height:31px}
.disclaimer{left:0;width:1200px;text-align:center;color:var(--white);font:600 9.5px/16px "Nunito Sans",sans-serif;text-transform:uppercase}
.foot-rule{left:76px;top:2596px;width:1048px;height:1px;background:#8a93a8}
</style>
</head>
<body>

<div class="abs topbar">Lorem ipsum dolor sit amet, consectetur adipisicing elit, sed do eiusmod tempor incididunt ut labore et dolore</div>

<header class="abs header">
  <div class="abs brand"><div class="brand-mark"></div><div>Dorian Kessel Law<small>A Professional Corporation</small></div></div>
  <div class="abs info" style="left:506px;top:24px">
    <svg width="28" height="38" viewBox="0 0 28 38" aria-hidden="true"><path d="M14 0C6.3 0 0 6.2 0 13.8 0 24 14 38 14 38s14-14 14-24.2C28 6.2 21.7 0 14 0z" fill="var(--gold)"/><circle cx="14" cy="13.5" r="5" fill="var(--navy)"/></svg>
    <div><div class="info-label">4820 West Harbor Avenue</div><div class="info-value">2207 Elk Grove, CA 95758</div></div>
  </div>
  <div class="abs info" style="left:870px;top:28px">
    <svg width="32" height="32" viewBox="0 0 32 32" aria-hidden="true"><rect width="32" height="32" rx="3" fill="var(--gold)"/><path d="M10 7l4 4-2.4 2.4c1.3 2.8 3.3 4.8 6 6L20 17l4 4-2.6 3c-7.4-.4-13-6-13.4-13.4z" fill="var(--navy)"/></svg>
    <div style="margin-left:34px"><div class="info-label">Free Consultation</div><div class="info-value">(916)555-0142</div></div>
  </div>
</header>

<nav class="abs nav">
  <a class="active" style="left:87px">Home</a>
  <a style="left:178px">Dorian Kessel</a>
  <a style="left:360px">Practice Areas</a>
  <a style="left:542px">Insights</a>
  <a style="left:664px">Contact.</a>
  <svg class="abs" style="left:1086px;top:20px" width="15" height="15" viewBox="0 0 15 15" aria-hidden="true"><circle cx="6" cy="6" r="4.5" fill="none" stroke="var(--gold)" stroke-width="2"/><path d="M9.5 9.5L14 14" stroke="var(--gold)" stroke-width="2.4" stroke-linecap="round"/></svg>
</nav>

<section class="abs hero" role="img" aria-label="Night skyline of downtown Sacramento with the gold lit tower bridge over the river">
  <h1>Sacramento Criminal &amp;<br>Civil Trial Attorney</h1>
</section>

<section class="abs services">
  <div class="abs card" style="left:75px;top:85px">
    <svg style="top:62px" width="72" height="66" viewBox="0 0 72 66" fill="none" stroke="var(--gold)" stroke-width="2.4"><path d="M4 20L36 3l32 17z"/><path d="M6 24h60M8 58h56M4 63h64"/><path d="M13 28v26M24 28v26M36 28v26M48 28v26M59 28v26"/></svg>
    <span style="top:168px">Criminal defence</span>
  </div>
  <div class="abs card" style="left:334px;top:85px">
    <svg style="top:58px" width="72" height="70" viewBox="0 0 72 70" fill="none" stroke="var(--gold)" stroke-width="2.4"><path d="M30 6l18 18-10 10-18-18z"/><path d="M40 30l24 24a4 4 0 0 1-6 6L34 36"/><path d="M4 62h44v6H4zM10 62v-6h32v6"/></svg>
    <span style="top:164px">Civil Litigation</span>
  </div>
  <div class="abs card" style="left:75px;top:330px">
    <svg style="top:62px" width="66" height="62" viewBox="0 0 66 62" fill="none" stroke="var(--gold)" stroke-width="2.2"><path d="M64 2L20 30l12 6 4 16 8-12 12 4z"/><path d="M64 2L32 36"/><path d="M14 40L4 50M20 46L8 58M12 34l-8 6" stroke-dasharray="3 3"/></svg>
    <span style="top:150px">Immigration</span>
  </div>
  <div class="abs card" style="left:334px;top:330px">
    <svg style="top:54px" width="64" height="70" viewBox="0 0 64 70" fill="none" stroke="var(--gold)" stroke-width="2.2"><circle cx="18" cy="14" r="10"/><circle cx="46" cy="14" r="10"/><circle cx="32" cy="38" r="9"/><path d="M4 48c0-10 6-16 14-16M60 48c0-10-6-16-14-16M18 66c0-9 6-14 14-14s14 5 14 14z"/></svg>
    <span style="top:150px">Family Laws</span>
  </div>

  <div class="abs intro" style="top:95px">
    <h2>Dorian Kessel law is a law firm serving the Sacramento Yolo, Contra Costa, and Stanislaus counties, San Joaquin Solako. We represents clients in a wide array of criminal, civil, family law and immigration cases.</h2>
    <p>Nemo enim ipsam voluptatem quia voluptas sit aspernatur aut odit aut fugit, sed quia consequuntur magni dolores eos qui ratione voluptatem sequi nesciunt.</p>
    <p>Neque porro quisquam est, qui dolorem ipsum quia dolor sit amet, consectetur, adipisci velit, sed quia non numquam eius modi tempora incidunt ut labore et dolore magnam aliquam quaerat voluptatem.</p>
  </div>
  <div class="abs rule" style="left:682px;top:481px;width:442px"></div>
  <div class="abs call-label" style="left:681px;top:507px">Call Dorian Kessel Today!</div>
  <div class="abs call-phone" style="left:681px;top:524px">(916)555-0142</div>
</section>

<section class="abs about" role="img" aria-label="Marble courthouse columns and carved ceiling seen from below"></section>
<div class="abs portrait" role="img" aria-label="Portrait of the attorney in a dark suit and tie"></div>
<div class="abs about-panel">
  <h2>Ready,Reliable and Experienced</h2>
  <p>Lorem ipsum dolor sit amet, consectetur adipisicing elit, sed do eiusmod tempor incididunt ut labore et dolore magna aliqua. Ut enim ad minim veniam, quis nostrud exercitation ullamco laboris nisi ut aliquip ex ea commodo consequat. Duis aute irure dolor in reprehenderit in voluptate velit esse cillum dolore eu fugiat nulla pariatur.</p>
  <span class="btn">About Dorian Kessel</span>
</div>

<section class="abs consult">
  <h2>Schedule A Free Consultation</h2>
</section>
<div class="abs field-label" style="left:75px;top:1963px">First Name *</div>
<div class="abs field-label" style="left:432px;top:1963px">Last Name *</div>
<div class="abs field" style="left:75px;top:1981px;width:334px;height:49px">First Name</div>
<div class="abs field" style="left:433px;top:1981px;width:333px;height:49px">Last Name</div>
<div class="abs field area" style="left:790px;top:1981px;width:334px;height:80px">Please Enter A brief description of your Case</div>
<div class="abs field-label" style="left:75px;top:2062px">Email *</div>
<div class="abs field-label" style="left:432px;top:2062px">Phone Number *</div>
<div class="abs field" style="left:75px;top:2078px;width:334px;height:49px">Email</div>
<div class="abs field" style="left:433px;top:2078px;width:333px;height:49px">Phone</div>
<div class="abs btn submit">Submit</div>

<footer class="abs footer">
  <div class="abs brand"><div class="brand-mark" style="width:58px;height:58px"></div><div style="font-size:16px">Dorian Kessel Law<small>A Professional Corporation</small></div></div>
  <div class="abs foot-head" style="left:682px;top:66px">Contact Info</div>
  <div class="abs foot-text" style="left:683px;top:105px">4820 West Harbor Ave suite<br>#2207 Elk Grove, CA 95758</div>
  <div class="abs foot-head" style="left:985px;top:64px">Quick Links</div>
  <div class="abs links" style="left:986px;top:104px">
    <a>Home</a><a>Dorian Kessel</a><a>Practice Areas</a><a>Insights</a><a>Contact</a>
  </div>
</footer>
<div class="abs disclaimer" style="top:2541px">This information on this website is for general purpose only. Nothing on this site should be taken as legal advice for any individual case or sitiation.<br>This is not intended to create, and receipt or viewing does not constitute an attorney client relationship</div>
<div class="abs foot-rule"></div>
<div class="abs disclaimer" style="top:2632px">Copyright 2021 all rights reserved</div>

</body>
</html>
```